Need DL Flyer for Real Estate Drops

We need a real estate flyer ,double sided. With content on 1 side like: Want to know what's your house is worth " contact us today and on other side agent details. We are looking for an ongoing partnership with designer so this assignment will be ongoing

```html
<!DOCTYPE html>
<html lang="en">
<head>
<meta charset="utf-8">
<title>Meridian Realty – DL Flyer</title>
<link href="https://fonts.googleapis.com/css2?family=Archivo+Black&family=Oswald:wght@600;700&family=Roboto:wght@300;400;700&family=Roboto+Condensed:wght@700&display=swap" rel="stylesheet">
<style>
:root{
  --navy:#1b2466;
  --red:#cf1f2e;
  --white:#ffffff;
  --paper:#f0f0f0;
  --ink:#1a1a1a;
  --stage:#ffffff;
  --sky-top:#2f4fb0;
  --sky-low:#8fb0e6;
  --grass:#4f8a2e;
}
*{margin:0;padding:0;box-sizing:border-box}
html,body{width:765px;height:1200px;overflow:hidden;background:var(--stage)}
body{position:relative;font-family:"Roboto",Arial,sans-serif;color:var(--ink)}
.flyer{position:absolute;top:255px;width:345px;height:690px;background:var(--white);overflow:hidden;box-shadow:0 2px 6px rgba(0,0,0,.25)}
.flyer--front{left:25px}
.flyer--back{left:395px}
.abs{position:absolute}
.photo{position:absolute}
.band{position:absolute;left:0;width:100%}
.band--navy{background:var(--navy)}
.band--red{background:var(--red)}
.band--paper{background:var(--paper)}

.brand{position:absolute;display:flex;align-items:center;gap:7px}
.brand__mark{width:22px;height:22px;background:var(--red)}
.brand__name{font-family:"Roboto",sans-serif;font-weight:400;font-size:26px;line-height:1;letter-spacing:.5px}
.brand--light .brand__name{color:var(--white)}
.brand--dark .brand__name{color:var(--navy)}

.headline{position:absolute;left:0;width:100%;text-align:center;top:300px;line-height:1}
.headline__top{font-family:"Archivo Black",sans-serif;font-size:30px;color:var(--red);letter-spacing:.5px}
.headline__mid{font-family:"Roboto",sans-serif;font-weight:300;font-size:31px;color:var(--ink);margin-top:-1px}
.headline__bot{font-family:"Oswald",sans-serif;font-weight:700;font-size:33px;color:var(--red);margin-top:-2px;transform:scaleY(1.05)}
.intro{position:absolute;left:20px;width:305px;top:390px;text-align:center;font-size:10.6px;line-height:13px;font-weight:400;color:#222}

.listing{position:absolute;border:1.5px solid var(--red)}
.listing__img{position:absolute;inset:0}
.listing__tag{position:absolute;left:-4px;right:0;bottom:0;height:22px;background:var(--navy);color:var(--white);font-family:"Roboto",sans-serif;font-weight:700;font-size:15px;padding-left:13px;line-height:22px}

.cta{position:absolute;left:0;width:100%;text-align:center;color:var(--white);font-family:"Roboto Condensed",sans-serif;font-weight:700}
.cta--call{top:583px;height:44px;line-height:44px;font-size:24px;display:flex;justify-content:center;align-items:center;gap:7px}
.cta--web{top:627px;height:63px;line-height:63px;font-size:21px;letter-spacing:.3px}

.bio{position:absolute;left:23px;top:340px;width:140px;font-size:9px;line-height:11.5px;color:#222}
.agent-photo{position:absolute;left:22px;top:414px;width:128px;height:276px;border-radius:60px 60px 0 0}
.agent-name{position:absolute;left:164px;top:415px;background:var(--navy);color:var(--white);font-family:"Oswald",sans-serif;font-weight:600;font-size:13px;padding:2px 5px;line-height:16px;letter-spacing:.3px}
.agent-name em{font-style:normal;color:var(--red)}
.agent-role{position:absolute;left:163px;top:440px;font-size:9.4px;font-weight:700;line-height:11px;color:#222}
.social{position:absolute;top:445px;display:flex;gap:4px;left:286px}
.social span{width:14px;height:14px;border-radius:50%;background:var(--red)}
.rule{position:absolute;left:163px;top:471px;width:160px;height:1px;background:#bbb}
.contact{position:absolute;left:163px;font-size:8px;font-weight:700;display:flex;align-items:center;gap:5px;line-height:9.5px;color:#111}
.contact--red{color:var(--red)}
.ico{width:13px;height:13px;flex:none}
.pitch{position:absolute;left:165px;top:595px;width:160px;font-size:9.4px;line-height:11.5px;color:var(--white)}
.pitch b{font-weight:700}
</style>
</head>
<body>

<!-- FRONT -->
<section class="flyer flyer--front">
  <div class="photo" role="img" aria-label="Photo of a single-storey brick house with garage and front lawn at dusk" style="left:0;top:0;width:345px;height:247px;background:linear-gradient(180deg,var(--sky-top) 0%,var(--sky-low) 42%,#8a8174 55%,#6b675f 78%,var(--grass) 88%,#7b4a32 100%)"></div>
  <svg class="abs" style="left:0;top:0" width="345" height="280" viewBox="0 0 345 280" aria-hidden="true">
    <path d="M345 222 A26 26 0 0 0 319 248 L331 248 A14 14 0 0 1 345 234 Z" fill="var(--red)"/>
    <path d="M0 254 L35 254 A35 35 0 0 1 0 289 L0 277 A23 23 0 0 0 23 254 Z" fill="var(--navy)"/>
  </svg>
  <div class="brand brand--light" style="left:85px;top:33px">
    <span class="brand__mark"></span><span class="brand__name">meridian</span>
  </div>
  <div class="band band--navy" style="top:247px;height:7px"></div>

  <div class="headline">
    <div class="headline__top">WANT TO KNOW</div>
    <div class="headline__mid">WHAT'S YOUR</div>
    <div class="headline__bot">HOUSE IS WORTH</div>
  </div>
  <p class="intro">Meridian Realty is established in 2017 and has a dynamic team of sales and rentals. We are committed to the continuous professional development of all our team and employ the latest technology tools to provide an accurate, timely experience for our clients.</p>

  <div class="band band--paper" style="top:462px;height:118px"></div>
  <div class="listing" style="left:23px;top:469px;width:144px;height:94px">
    <div class="listing__img" role="img" aria-label="Photo of a sold single-storey home" style="background:linear-gradient(180deg,#9bb6d9 0%,#cfd6dc 40%,#8d7a66 65%,#5b8a3a 100%)"></div>
    <div class="listing__tag">SOLD</div>
  </div>
  <div class="listing" style="left:178px;top:469px;width:144px;height:94px">
    <div class="listing__img" role="img" aria-label="Photo of a sold brick home lit at dusk" style="background:linear-gradient(180deg,#7f9fd0 0%,#c9c2b5 40%,#8a5e3d 70%,#b8b4ad 100%)"></div>
    <div class="listing__tag">SOLD</div>
  </div>

  <div class="band band--red" style="top:583px;height:44px"></div>
  <div class="band band--navy" style="top:627px;height:63px"></div>
  <div class="cta cta--call">Call us
    <svg class="ico" style="width:20px;height:20px" viewBox="0 0 24 24" aria-hidden="true"><path d="M6.6 10.8a15 15 0 0 0 6.6 6.6l2.2-2.2c.3-.3.7-.4 1-.2 1.1.4 2.3.6 3.6.6.6 0 1 .4 1 1V20c0 .6-.4 1-1 1A17 17 0 0 1 3 4c0-.6.4-1 1-1h3.5c.6 0 1 .4 1 1 0 1.3.2 2.5.6 3.6.1.3 0 .7-.2 1z" fill="var(--white)"/></svg>
    03 9000 1234</div>
  <div class="cta cta--web">www.meridianrealty.com.au</div>
</section>

<!-- BACK -->
<section class="flyer flyer--back">
  <div class="photo" role="img" aria-label="Photo of a modern brick home with lit windows, lawn and concrete path" style="left:0;top:0;width:345px;height:314px;background:linear-gradient(180deg,#5b86d6 0%,#a9c3ea 30%,#8a6a52 48%,#5d5349 66%,#5f8a3a 80%,#c9c9c6 100%)"></div>
  <div class="listing" style="left:191px;top:20px;width:130px;height:85px">
    <div class="listing__img" role="img" aria-label="Photo of a white kitchen interior" style="background:linear-gradient(180deg,#f3f3f3 0%,#dcdcdc 60%,#3a3a3a 100%)"></div>
    <div class="listing__tag">SOLD</div>
  </div>
  <div class="listing" style="left:191px;top:116px;width:130px;height:85px">
    <div class="listing__img" role="img" aria-label="Photo of a sold modern home exterior" style="background:linear-gradient(180deg,#5c86d0 0%,#d8d6d0 45%,#7a6052 75%,#5f8a3a 100%)"></div>
    <div class="listing__tag">SOLD</div>
  </div>
  <div class="listing" style="left:191px;top:211px;width:130px;height:85px">
    <div class="listing__img" role="img" aria-label="Photo of a bathroom with glass shower" style="background:linear-gradient(90deg,#eaeaea 0%,#d5d7d8 55%,#2d2d2d 100%)"></div>
    <div class="listing__tag">SOLD</div>
  </div>
  <svg class="abs" style="left:0;top:270px" width="345" height="50" viewBox="0 0 345 50" aria-hidden="true">
    <path d="M345 14 A30 30 0 0 0 315 44 L328 44 A17 17 0 0 1 345 27 Z" fill="var(--red)"/>
    <path d="M0 20 A24 24 0 0 1 24 44 L14 44 A14 14 0 0 0 0 30 Z" fill="var(--navy)"/>
  </svg>
  <div class="band band--navy" style="top:314px;height:7px"></div>

  <p class="bio">A passionate Cricketer, Daniel is a highly motivated and energetic individual who strives for success.</p>
  <div class="brand brand--dark" style="left:180px;top:350px">
    <span class="brand__mark"></span><span class="brand__name">meridian</span>
  </div>

  <div class="band band--paper" style="top:400px;height:183px"></div>
  <div class="band band--red" style="top:586px;height:74px"></div>
  <div class="band band--navy" style="top:660px;height:30px"></div>

  <div class="agent-photo" role="img" aria-label="Portrait of the agent in a navy suit" style="background:linear-gradient(180deg,#c9a58a 0%,#b48d72 22%,#2b3550 30%,#1f2740 100%)"></div>

  <div class="agent-name"><em>DANIEL</em> ASHFORD</div>
  <div class="agent-role">Managing Director/lea,<br>Meridian Realty</div>
  <div class="social" aria-hidden="true"><span></span><span></span></div>
  <div class="rule"></div>

  <div class="contact contact--red" style="top:479px">
    <svg class="ico" viewBox="0 0 24 24" aria-hidden="true"><circle cx="12" cy="12" r="12" fill="var(--navy)"/><path d="M8.6 10.9a9 9 0 0 0 4.5 4.5l1.5-1.5c.2-.2.5-.3.7-.1.7.2 1.5.4 2.3.4.4 0 .7.3.7.7V17c0 .4-.3.7-.7.7A11.7 11.7 0 0 1 6.3 6.4c0-.4.3-.7.7-.7h2.3c.4 0 .7.3.7.7 0 .8.1 1.6.4 2.3 0 .3 0 .5-.2.7z" fill="var(--white)"/></svg>
    (03) 9000 1234
    <svg class="ico" style="margin-left:4px" viewBox="0 0 24 24" aria-hidden="true"><circle cx="12" cy="12" r="12" fill="var(--navy)"/><path d="M8.6 10.9a9 9 0 0 0 4.5 4.5l1.5-1.5c.2-.2.5-.3.7-.1.7.2 1.5.4 2.3.4.4 0 .7.3.7.7V17c0 .4-.3.7-.7.7A11.7 11.7 0 0 1 6.3 6.4c0-.4.3-.7.7-.7h2.3c.4 0 .7.3.7.7 0 .8.1 1.6.4 2.3 0 .3 0 .5-.2.7z" fill="var(--white)"/></svg>
    0400111222
  </div>
  <div class="contact" style="top:500px">
    <svg class="ico" viewBox="0 0 24 24" aria-hidden="true"><circle cx="12" cy="12" r="12" fill="var(--navy)"/><circle cx="12" cy="12" r="6" fill="none" stroke="var(--white)" stroke-width="1.4"/><path d="M6 12h12M12 6c-2.5 3-2.5 9 0 12M12 6c2.5 3 2.5 9 0 12" fill="none" stroke="var(--white)" stroke-width="1.2"/></svg>
    www.meridianrealty.com.au
  </div>
  <div class="contact" style="top:520px">
    <svg class="ico" viewBox="0 0 24 24" aria-hidden="true"><circle cx="12" cy="12" r="12" fill="var(--navy)"/><rect x="6" y="8" width="12" height="8.5" rx="1" fill="none" stroke="var(--white)" stroke-width="1.4"/><path d="M6.5 8.7 12 13l5.5-4.3" fill="none" stroke="var(--white)" stroke-width="1.3"/></svg>
    daniel@meridianrealty.com.au
  </div>
  <div class="contact" style="top:540px;align-items:flex-start">
    <svg class="ico" viewBox="0 0 24 24" aria-hidden="true"><circle cx="12" cy="12" r="12" fill="var(--navy)"/><path d="M12 5.5a4.5 4.5 0 0 0-4.5 4.5c0 3.3 4.5 8.5 4.5 8.5s4.5-5.2 4.5-8.5A4.5 4.5 0 0 0 12 5.5z" fill="var(--white)"/><circle cx="12" cy="10" r="1.6" fill="var(--navy)"/></svg>
    <span>14/8 Harbour Rd, Westbrook,<br>VIC 3999</span>
  </div>

  <p class="pitch"><b>Daniel</b> has a fierce desire to be successful at what he does and constantly raises the bar to attain the high standards</p>
</section>

</body>
</html>
```